Halt and Thicken New Branding Stationary Set - updated Oct 30th 2017

Updated on 30th Oct 2017 as we now need a whole folder design instead of a folder cover. We have thought out exactly what should be on it so it wont be hard. We are happy for this to be completed only by the winning designer if you like. And also we are guaranteeing this project now. Thanks!

We just got our new logo and now we would like a stationary set so we can brand our company communications. The items we need designed are:
Business cards
Letterhead
Appointment confirmation cards
Folder - switched from folder cover. Note that if you don't wish to do this unless you are selected as the winner this is fine.

1. Business cards - for 5 employees, final names will be given once the winner is selected, but you can use this one as the sample:
Lucinda Prieto
Hair Regrowth Expert
Halt and Thicken
7127 Marbury Ave, Suite 500
Kestrel Park CA 90877
lucinda@gavinthorpemd.example
(555) 238-9016

2. Letterhead 8.5" x 11.0" vertical
Halt and Thicken
Kestrel Park CA 90877
office@haltandthicken.example
(555) 238-9016

3. Appointment Confirmation cards - business card size
Halt and Thicken
Kestrel Park CA 90877
Appointment For:
Date:
Time:
If you are unable to make your appointment, please contact us to reschedule at:
(555) 238-9016
info@gavinthorpemd.example

*UPDATED*
4. Folder 9" x 12 " vertical with double pocket
We would like the infinity image from the logo made really big so the left side is on the back and the right side with the + sign is on the front and its takes up the maximum room on the folder.
On the front below the half logo it should say "A Biochemical Revolution..."
On the inside we would also like to have the infinity sign from the logo but faded and half on the left pocket half on the right.
On left inside pocket it should say (this will be partically written on top of the logo):
Gavin Thorpe MD
Precision Medicine
Halt and Thicken Hair
On the Right inside pocket it should say the following:
Because the Enemy of BETTER Health is Good Health
BETTER Ingredients
BETTER Recipe
BETTER Medicine
On the back below the logo on the bottom should be the contact information.
I attached a picture of our drawing of what we want for this to make it easier.

Here is our website to give you an idea of our branding: http://www.haltandthicken.example/

We are the only true cure for hair loss and need to look professional and highest quality and beyond reproach from an ethical standpoint. We are a medical clinic so this should be portrayed also.
We cured hair loss by analyzing biochemistry and rebalancing it so that the process reverses and your own hair can grow back naturally.

Business card information:

OK so here is the information for the business cards:

Lucinda Prieto
Hair Regrowth Expert
(555) 238-9016
www.haltandthicken.example

Marisol Quintero
Hair Growth Consultant
(555) 238-9016
marisol@gavinthorpemd.example
www.haltandthicken.example

Glenda Hutchins
CMO/COO
(555) 238-9016
glenda@haltandthicken.example
www.haltandthicken.example

Dr Lou Thorpe
President
(555) 238-9016
info@gavinthorpemd.example
www.haltandthicken.example

Halt and Thicken
Customer Service
(555) 238-9016
info@gavinthorpemd.example
www.haltandthicken.example

Target Market(s)

Men aged 20-24 who care about their appearance, care about their hair and care about the world.

Industry/Entity Type

Medical And Science

Font styles to use
Sans Serif

Colors
00a990
ffffff
9d9d9d
333333

Requirements
Must have
• Must use the logo and our brand colors from the logo in all designs.
• The pantone colors are:
• Green: #4ca26f
• Light Grey: #999999
• The design should be symmetrical and balanced.
Nice to have
• It should look reasonably masculine.
Should not have
• Do not include any red in the design.

```html
<!DOCTYPE html>
<html lang="en">
<head>
<meta charset="utf-8">
<title>Halt and Thicken – Appointment Card</title>
<link rel="stylesheet" href="https://fonts.googleapis.com/css2?family=Open+Sans:wght@400;600&display=swap">
<style>
  :root {
    --green: #4ca26f;
    --grey: #999999;
    --ink: #333333;
    --rule: #9d9d9d;
    --paper: #ffffff;
    --backdrop: #1c1c1c;
  }
  * { box-sizing: border-box; margin: 0; padding: 0; }
  html, body {
    width: 1200px; height: 1200px; overflow: hidden;
    background: var(--backdrop);
    font-family: "Open Sans", sans-serif;
    color: var(--ink);
  }
  .appointment-card {
    position: absolute; left: 75px; top: 300px;
    width: 1050px; height: 600px;
    background: var(--paper);
  }
  .brand {
    position: absolute; left: 64px; top: 152px;
    display: flex; align-items: center; gap: 14px;
  }
  .brand-dot { width: 22px; height: 22px; border-radius: 50%; background: var(--green); }
  .brand-name { font-size: 30px; font-weight: 400; color: var(--ink); }
  .address {
    position: absolute; left: 640px; top: 66px;
    border-left: 4px solid var(--green);
    padding-left: 16px;
    font-size: 20px; line-height: 28px; color: #555;
    font-style: normal;
  }
  .field { position: absolute; font-size: 30px; color: var(--ink); }
  .field-small { font-size: 26px; }
  .rule { position: absolute; height: 2px; background: var(--rule); }
  .days {
    position: absolute; left: 60px; top: 420px; width: 950px;
    display: flex; justify-content: space-between;
    font-size: 30px; list-style: none;
  }
  .days li { display: flex; align-items: center; gap: 10px; }
  .checkbox { width: 26px; height: 26px; border: 3px solid var(--green); }
  .notice {
    position: absolute; left: 0; right: 0; top: 505px;
    text-align: center; font-size: 22px; color: var(--ink);
  }
  .contact {
    position: absolute; left: 0; right: 0; top: 545px;
    display: flex; justify-content: center; gap: 36px;
    font-size: 22px; color: var(--ink);
  }
  .contact span { display: flex; align-items: center; gap: 8px; }
</style>
</head>
<body>
  <section class="appointment-card">
    <div class="brand">
      <span class="brand-dot"></span>
      <span class="brand-name">Halt and Thicken</span>
    </div>

    <address class="address">
      Halt and Thicken<br>
      7127 Marbury Ave, Suite 500<br>
      Kestrel Park CA 90877
    </address>

    <span class="field" style="left:60px; top:265px;">Name</span>
    <span class="rule" style="left:170px; top:300px; width:830px;"></span>

    <span class="field" style="left:60px; top:335px;">Date</span>
    <span class="rule" style="left:160px; top:370px; width:300px;"></span>
    <span class="field" style="left:490px; top:335px;">Time</span>
    <span class="rule" style="left:580px; top:370px; width:260px;"></span>
    <span class="field field-small" style="left:855px; top:330px;">A.M.</span>
    <span class="field field-small" style="left:940px; top:330px;">P.M.</span>

    <ul class="days">
      <li><span class="checkbox"></span>Mon.</li>
      <li><span class="checkbox"></span>Tues.</li>
      <li><span class="checkbox"></span>Wed.</li>
      <li><span class="checkbox"></span>Thurs.</li>
      <li><span class="checkbox"></span>Fri.</li>
      <li><span class="checkbox"></span>Sat.</li>
    </ul>

    <p class="notice">If you are unable to make your appointment, please contact us to reschedule at</p>
    <div class="contact">
      <span>
        <svg width="18" height="22" viewBox="0 0 18 22" aria-hidden="true">
          <path d="M5 2 L9 7 L6 10 Q8 14 11 16 L14 13 L17 17 L14 20 Q4 17 2 5 Z" fill="var(--green)"/>
        </svg>
        (555) 238-9016
      </span>
      <span>
        <svg width="22" height="16" viewBox="0 0 22 16" aria-hidden="true">
          <rect x="1" y="1" width="20" height="14" fill="var(--green)"/>
          <path d="M1 1 L11 9 L21 1" fill="none" stroke="#fff" stroke-width="2"/>
        </svg>
        info@gavinthorpemd.example
      </span>
    </div>
  </section>
</body>
</html>
```